Cedar Hollow responsive web design

We need a responsive, bootstrap compatible (but design only - PSD files) website design for a fly fishing shop and guide service.

Design should be very clean. Home Page design + interior page design please.

Possible Home Page Content:
Slide Show
Highlight Three Features: Guided Trips, Fly Shop, Missouri River
About

Thank you and good luck!

Shop

• This will be used on Bootstrap CMS so needs 12 column bootstrap measurements.

DESIGN ONLY NEEDED (clean PSD files), no programming required.
Need a Home Page layout and secondary page layout

Must show use of the following:
H1 - H5 font uses
link color
Dropdown for navigation bar
Button example
• No cutout images, this will be part of CMS and client needs to be able to update most content without knowing photoshop.

```html
<!DOCTYPE html>
<html lang="en">
<head>
<meta charset="utf-8">
<title>Cedar Hollow — Fly Shop &amp; Guide Service</title>
<link href="https://fonts.googleapis.com/css2?family=Open+Sans:ital,wght@0,400;0,700;0,800;1,600&display=swap" rel="stylesheet">
<style>
  :root {
    --page-bg: #ffffff;
    --nav-band: #ebebeb;
    --nav-text: #1e1e1e;
    --ink: #222222;
    --body-text: #333333;
    --accent-orange: #f08a2e;
    --accent-sky: #7fcbea;
    --footer-band: #7890b0;
    --white: #ffffff;
    --dot-fill: #7fb8cf;
  }
  * { box-sizing: border-box; margin: 0; padding: 0; }
  html, body { width: 1200px; height: 1000px; overflow: hidden; background: var(--page-bg); }
  body { position: relative; font-family: "Open Sans", Arial, sans-serif; color: var(--ink); }

  .nav-band { position: absolute; left: 0; top: 60px; width: 1200px; height: 57px; background: var(--nav-band); }
  .nav-list { position: absolute; top: 82px; display: flex; list-style: none; font-size: 10px; text-transform: uppercase; color: var(--nav-text); }
  .nav-list li { line-height: 12px; white-space: nowrap; }
  .nav-left { left: 208px; width: 267px; justify-content: space-between; }
  .nav-right { left: 724px; width: 267px; justify-content: space-between; }
  .nav-list .is-active { border-bottom: 1px solid var(--nav-text); padding-bottom: 3px; }

  .brand-box { position: absolute; left: 500px; top: 50px; width: 197px; height: 78px; background: var(--white);
    box-shadow: 0 1px 3px rgba(0,0,0,.35); display: flex; align-items: center; justify-content: center; gap: 8px; }
  .brand-box .brand-mark { width: 12px; height: 12px; background: var(--accent-sky); }
  .brand-box .brand-name { font-size: 17px; font-weight: 700; color: var(--nav-text); }

  .hero { position: absolute; left: 0; top: 180px; width: 1200px; height: 381px;
    background: linear-gradient(180deg, #6f7680 0%, #8a7f70 28%, #b07a3e 42%, #8a6a4c 55%, #5d6470 75%, #4d5562 100%); }
  .hero-ring { position: absolute; left: 510px; top: 55px; width: 176px; height: 176px; border: 4px solid var(--white); border-radius: 50%; }
  .hero-headline { position: absolute; left: 510px; top: 119px; width: 176px; text-align: center;
    font-size: 34px; line-height: 44px; font-style: italic; font-weight: 600; color: var(--white); }
  .hero-subline { position: absolute; left: 400px; top: 242px; width: 400px; text-align: center;
    font-size: 21px; line-height: 28px; font-weight: 800; letter-spacing: .5px; text-transform: uppercase; color: var(--white); }

  .slider-dots { position: absolute; left: 565px; top: 528px; display: flex; gap: 11px; }
  .slider-dots span { width: 14px; height: 14px; border-radius: 50%; border: 2px solid var(--white); background: var(--dot-fill); }
  .slider-dots span.is-current { background: transparent; }

  .quote-bar { position: absolute; left: 209px; top: 589px; width: 783px; height: 62px; background: var(--accent-orange);
    color: var(--white); font-size: 17px; line-height: 22px; }
  .quote-bar .quote-text { position: absolute; left: 229px; top: 11px; }
  .quote-bar .quote-author { position: absolute; left: 428px; top: 35px; }
  .quote-pointer { position: absolute; left: 592px; top: 651px; width: 0; height: 0;
    border-left: 10px solid transparent; border-right: 10px solid transparent; border-top: 11px solid var(--accent-orange); }

  .feature { position: absolute; top: 673px; width: 180px; }
  .feature-image { width: 180px; height: 98px; display: flex; align-items: center; justify-content: center;
    color: var(--white); font-size: 17px; }
  .feature-title { margin-top: 17px; text-align: center; font-weight: 400; font-size: 16px; letter-spacing: .4px; text-transform: uppercase; }
  .feature-copy { margin-top: 6px; font-size: 10px; line-height: 12px; color: var(--body-text); }

  .feature-proshop { left: 209px; }
  .feature-location { left: 410px; }
  .feature-heading { left: 611px; }
  .feature-outfitters { left: 812px; }
  .img-proshop { background: linear-gradient(135deg, #b9ab7d, #7d8b86 60%, #5b6f6b); }
  .img-location { background: linear-gradient(180deg, #a9bfd6 0%, #c7d3df 55%, #8f8a7c 75%, #6e6a62 100%); }
  .img-sunset { background: linear-gradient(180deg, #2e2a4a 0%, #c85a2a 40%, #f0a03a 55%, #3a3040 80%, #1c1f2c 100%); }
  .img-outfitters { background: linear-gradient(135deg, #6d7a70, #8c8f74 50%, #4e5e5a); }

  .promo-band { position: absolute; left: 208px; top: 943px; width: 783px; height: 57px; background: var(--footer-band); overflow: hidden; }
  .promo-band h1 { position: absolute; left: 16px; top: 6px; font-size: 42px; font-weight: 800; letter-spacing: -.5px; color: var(--white); line-height: 60px; white-space: nowrap; }
  .promo-band h3 { position: absolute; left: 242px; top: 29px; font-size: 20px; font-style: italic; font-weight: 600; color: var(--white); white-space: nowrap; }
  .promo-link { position: absolute; left: 365px; top: 17px; font-size: 13px; font-weight: 700; color: #1f2a3a; }
  .btn { position: absolute; top: 18px; width: 103px; height: 40px; border: 2px solid var(--white); border-radius: 3px;
    color: var(--white); font-size: 16px; text-align: center; line-height: 36px; }
  .btn-sky { left: 514px; background: var(--accent-sky); }
  .btn-orange { left: 659px; background: var(--accent-orange); }
</style>
</head>
<body>
  <header>
    <div class="nav-band"></div>
    <ul class="nav-list nav-left">
      <li class="is-active">Home</li><li>About</li><li>Services</li><li>Products</li><li>Gallery</li>
    </ul>
    <div class="brand-box"><span class="brand-mark"></span><span class="brand-name">Cedar Hollow</span></div>
    <ul class="nav-list nav-right">
      <li>Testimonials</li><li>Shop</li><li>FAQ</li><li>Find Us</li><li>Contact</li>
    </ul>
  </header>

  <section class="hero">
    <div class="hero-photo" role="img" aria-label="Slide photo: calm river at sunset with mountains and trees reflected in the water"></div>
    <div class="hero-ring"></div>
    <h2 class="hero-headline">Freedom</h2>
    <p class="hero-subline">Is the oxygen of the soul</p>
  </section>
  <div class="slider-dots"><span></span><span class="is-current"></span><span></span></div>

  <section class="quote-bar">
    <span class="quote-text">“BIG QUOTE GOES HERE! Lorem Ipsum...”</span>
    <span class="quote-author">- Elias Corwin</span>
  </section>
  <div class="quote-pointer"></div>

  <article class="feature feature-proshop">
    <div class="feature-image img-proshop" role="img" aria-label="Photo of the fly shop interior with stocked shelves"></div>
    <h4 class="feature-title">Proshop</h4>
    <p class="feature-copy">Phasellus facilisis, nunc in lacinia auctor, eros lacus aliquet velit, quis lobortis risus nunc nec nisi. Maecenas et turpis vitae velit volutpat porttitor a sit amet est. Uthasellus facilisis, nunc in lacinia auctor, eros lacus aliquet velit, quis lobortis risus nunc nec nisi.</p>
  </article>
  <article class="feature feature-location">
    <div class="feature-image img-location" role="img" aria-label="Photo of the shop building exterior with a boat trailer"></div>
    <h4 class="feature-title">Location</h4>
    <p class="feature-copy">Phasellus facilisis, nunc in lacinia auctor, eros lacus aliquet velit, quis lobortis risus nunc nec nisi. Maecenas et turpis vitae velit volutpat porttitor a sit amet est. Uthasellus facilisis, nunc in lacinia auctor, eros lacus aliquet velit, quis lobortis risus nunc nec nisi.</p>
  </article>
  <article class="feature feature-heading">
    <div class="feature-image img-sunset" role="img" aria-label="Photo of a vivid sunset over water"></div>
    <h4 class="feature-title">Heading</h4>
    <p class="feature-copy">Phasellus facilisis, nunc in lacinia auctor, eros lacus aliquet velit, quis lobortis risus nunc nec nisi. Maecenas et turpis vitae velit volutpat porttitor a sit amet est. Uthasellus facilisis, nunc in lacinia auctor, eros lacus aliquet velit, quis lobortis risus nunc nec nisi.</p>
  </article>
  <article class="feature feature-outfitters">
    <div class="feature-image img-outfitters" role="img" aria-label="Photo of the outfitters gear room">GEAR UP</div>
    <h4 class="feature-title">Outfitters</h4>
    <p class="feature-copy">Phasellus facilisis, nunc in lacinia auctor, eros lacus aliquet velit, quis lobortis risus nunc nec nisi. Maecenas et turpis vitae velit volutpat porttitor a sit amet est. Uthasellus facilisis, nunc in lacinia auctor, eros lacus aliquet velit, quis lobortis risus nunc nec nisi.</p>
  </article>

  <section class="promo-band">
    <h1>Heading 1</h1>
    <h3>Heading 3</h3>
    <span class="promo-link">www.riverpage.net</span>
    <span class="btn btn-sky">BUTTON</span>
    <span class="btn btn-orange">BUTTON</span>
  </section>
</body>
</html>
```